Dale Winslow Drum Demo

My husband and I just moved to Nashville. Dale (my husband) is a drummer with 30 years of experience. We have a CD that we would like to promote with hope that he can get a gig doing what he loves. We would like your talented artists to create a CD cover and label. We are here to promote Dale, although we also think the rest of the band should be mentioned and recognized. I am going to put the names of the musicians as well as two pictures that can be used for the outside cover if necessary. On the inside of the cover I would like the band members mentioned as well as a little bio. about Dale.
Dale Winslow - drums and vocals
Mark Delvey - vocals
Rick Hanlon - bass
Pete Morant - lead guitar

Dale's bio
Born in Massachusetts
30 years experience
some drumming school
local band experience
music played: blues, classic rock, country, jazz, and alternative
influences: Carl Mesner, Lenny Vask, Glen Fosk, Walt Dusek
Great passion, feel, and desire for music....something which cannot be taught!!!

```html
<!DOCTYPE html>
<html lang="en">
<head>
<meta charset="utf-8">
<title>Dale Winslow – CD Cover and Inlay</title>
<link rel="stylesheet" href="https://fonts.googleapis.com/css2?family=Roboto:wght@300;400;700&display=swap">
<style>
  :root {
    --page: #ffffff;
    --panel: #0b0b0b;
    --ink: #f2f2f2;
    --ink-soft: #bdbdbd;
    --rule: #d9d9d9;
    --warm-glow: #c98a3a;
    --warm-deep: #3a2410;
    --steel: #9a9a9a;
    --steel-deep: #2a2a2a;
    --wood: #c79a6a;
  }
  * { box-sizing: border-box; margin: 0; padding: 0; }
  html, body {
    width: 1200px; height: 1000px; overflow: hidden;
    background: var(--page);
    font-family: "Roboto", Arial, sans-serif;
  }
  .sheet { position: relative; width: 1200px; height: 1000px; }
  .panel { position: absolute; background: var(--panel); color: var(--ink); }
  .cover-kit   { left: 187px; top: 91px;  width: 415px; height: 398px; }
  .inlay-top   { left: 607px; top: 91px;  width: 393px; height: 398px; }
  .cover-snare { left: 187px; top: 509px; width: 410px; height: 397px; }
  .inlay-bottom{ left: 607px; top: 507px; width: 393px; height: 399px; }

  .photo { position: absolute; }
  .photo--kit {
    left: 25px; top: 50px; width: 360px; height: 285px;
    background: radial-gradient(ellipse at 55% 50%, var(--warm-glow) 0%, var(--warm-deep) 40%, var(--panel) 72%);
  }
  .photo--snare {
    left: 50px; top: 100px; width: 320px; height: 200px;
    background: radial-gradient(ellipse at 50% 50%, var(--wood) 0%, #5b4636 35%, #1c1c1c 65%, var(--panel) 80%);
  }
  .photo--cymbals {
    left: 213px; top: 224px; width: 170px; height: 150px;
    background: radial-gradient(ellipse at 55% 40%, #d8d8d8 0%, var(--steel) 30%, var(--steel-deep) 60%, var(--panel) 80%);
  }

  .artist-title {
    position: absolute; left: 37px; right: 35px; top: 351px;
    display: flex; align-items: center; gap: 10px;
    font-weight: 300; font-size: 12px; letter-spacing: 6.2px;
    white-space: nowrap;
  }
  .artist-title::before, .artist-title::after {
    content: ""; flex: 1; height: 1px; background: var(--rule);
  }

  .bio { position: absolute; left: 92px; top: 70px; width: 206px; }
  .bio__heading {
    text-align: center; font-weight: 700; font-size: 13px;
    letter-spacing: 3px; margin-bottom: 4px;
  }
  .bio__text {
    font-weight: 300; font-size: 9.6px; line-height: 11.8px;
    text-align: justify; text-align-last: left; margin-bottom: 10px;
  }
  .bio__text strong { font-weight: 700; }

  .band { position: absolute; left: 43px; top: 289px; }
  .band__label {
    font-size: 6px; letter-spacing: 4px; color: var(--ink-soft);
    margin-bottom: 9px;
  }
  .band__list { list-style: none; font-weight: 300; font-size: 9px; line-height: 11.6px; }
</style>
</head>
<body>
<main class="sheet">

  <section class="panel cover-kit">
    <div class="photo photo--kit" role="img" aria-label="Drum kit lit with warm golden light against black"></div>
    <h1 class="artist-title">DALE WINSLOW</h1>
  </section>

  <section class="panel inlay-top">
    <article class="bio">
      <h2 class="bio__heading">BIO</h2>
      <p class="bio__text">Born in Massachusetts 30 years experience some drumming schoollocal band experience</p>
      <p class="bio__text"><strong>Music played:</strong> blues, classic rock, country, jazz, and alternative influences: Carl Mesner, Lenny Vask, Glen Fosk, Walt Dusek Great passion, feel, and desire for music....something which cannot be taught!!!</p>
    </article>
    <div class="band">
      <p class="band__label">BAND MEMBERS:</p>
      <ul class="band__list">
        <li>Dale Winslow - drums and vocals</li>
        <li>Mark Delvey - vocals</li>
        <li>Rick Hanlon - bass</li>
        <li>Pete Morant - lead guitar</li>
      </ul>
    </div>
    <div class="photo photo--cymbals" role="img" aria-label="Black and white drum kit with cymbals seen from above"></div>
  </section>

  <section class="panel cover-snare">
    <div class="photo photo--snare" role="img" aria-label="Wooden snare drum and black snare drum on a reflective surface"></div>
    <h1 class="artist-title">DALE WINSLOW</h1>
  </section>

  <section class="panel inlay-bottom">
    <article class="bio">
      <h2 class="bio__heading">BIO</h2>
      <p class="bio__text">Born in Massachusetts 30 years experience some drumming schoollocal band experience</p>
      <p class="bio__text"><strong>Music played:</strong> blues, classic rock, country, jazz, and alternative influences: Carl Mesner, Lenny Vask, Glen Fosk, Walt Dusek Great passion, feel, and desire for music....something which cannot be taught!!!</p>
    </article>
    <div class="band">
      <p class="band__label">BAND MEMBERS</p>
      <ul class="band__list">
        <li>Dale Winslow - drums and vocals</li>
        <li>Mark Delvey - vocals</li>
        <li>Rick Hanlon - bass</li>
        <li>Pete Morant - lead guitar</li>
      </ul>
    </div>
    <div class="photo photo--cymbals" role="img" aria-label="Black and white drum kit with cymbals seen from above"></div>
  </section>

</main>
</body>
</html>
```